依頼概要
■依頼の目的/概要
コンサルティング業の中で「ほたる相談室」というテーマの中で、
営業力や対人対応力の向上支援などをお手伝いしています。
今回電子書籍出版にあたり、添付ファイルの書籍のイメージに沿うデザインを製作依頼させていただきます。

■書籍タイトル:『どうして?腕時計を磨くと来店客がふえるのか』
サブタイトル:「未来をひらくのは話術より笑顔力」

■本の内容
見た目が人に与える印象などについて記載したものになります。
営業マンのような個人の方や、法人教育に携わるような方にもお読みいただきたいものです。
詳細は添付ファイルを参照ください。

■デザイン要望
自由なご提案をおまちしております。
堅苦しくなく、気軽に手に取っていただけるようなデザインを希望です。

その他何かご不明な点がございましたら、お気軽にご質問下さい。
よろしくお願いいたします。
提案して頂いた皆様、私のミスで写真を2枚お送りできていませんでした。
大変申し訳ございませんがこの写真2枚を使って頂けますよう宜しくお願い致します。

この写真を使ってください
■ 選んだ理由

ネクタイの縦とメッセージの流れがとても良かったです。

■ 提案者全員のお礼・コメント

今回は、沢山の人にいろいろなデザインでご提案いただきありがとうございました。

```html
<!DOCTYPE html>
<html lang="ja">
<head>
<meta charset="utf-8">
<title>どうして?腕時計を磨くと来店客がふえるのか</title>
<link rel="stylesheet" href="https://fonts.googleapis.com/css2?family=Noto+Sans+JP:wght@400;700;900&display=swap">
<style>
  :root {
    --sky: #8fc2e8;
    --navy: #1e2c4f;
    --tie-dark: #2a3d66;
    --tie-mid: #4b6391;
    --tie-light: #6f8fbf;
    --paper: #ffffff;
    --ink: #222831;
    --orange: #e39236;
    --dash: #9a9a9a;
  }
  html, body { margin: 0; padding: 0; overflow: hidden; }
  body { width: 750px; height: 1200px; font-family: "Noto Sans JP", sans-serif; }
  .cover { position: relative; width: 750px; height: 1200px; background: var(--paper); overflow: hidden; }
  .sky { position: absolute; left: 0; top: 0; width: 750px; height: 885px; background: var(--sky); }
  .tie { position: absolute; top: 0; width: 30px; border-radius: 0 0 15px 15px; }
  .tie.dark { background: var(--tie-dark); }
  .tie.mid { background: var(--tie-mid); }
  .tie.light { background: var(--tie-light); }
  .author { position: absolute; left: 40px; top: 58px; color: var(--navy); }
  .author-name { font-size: 42px; font-weight: 700; letter-spacing: 4px; line-height: 1; }
  .author-roman { font-size: 15px; margin-top: 8px; letter-spacing: 0.5px; }
  .title { position: absolute; right: 40px; top: 30px; margin: 0; text-align: right; color: var(--navy); font-weight: 900; }
  .title-lead { font-size: 86px; line-height: 1.2; letter-spacing: 0; white-space: nowrap; }
  .title-line { font-size: 74px; line-height: 84px; letter-spacing: 6px; white-space: nowrap; }
  .title-lead + .title-line { margin-top: 18px; }
  .tagline { position: absolute; left: 52px; top: 918px; color: var(--ink); font-size: 33px; font-weight: 700; line-height: 1.4; }
  .keyword { position: absolute; left: 420px; top: 888px; width: 290px; height: 110px; border: 4px dashed var(--dash); box-sizing: border-box; display: flex; align-items: center; justify-content: center; font-size: 80px; font-weight: 900; color: var(--ink); letter-spacing: 2px; }
  .gift { position: absolute; top: 1035px; width: 330px; text-align: center; }
  .gift-1 { left: 28px; }
  .gift-2 { left: 395px; }
  .ribbon { display: block; margin: 0 auto; }
  .gift-note { font-size: 19px; color: var(--ink); margin-top: 10px; white-space: nowrap; }
  .gift-item { font-size: 26px; font-weight: 900; color: var(--ink); margin-top: 2px; white-space: nowrap; }
</style>
</head>
<body>
<div class="cover">
  <div class="sky"></div>

  <div class="tie mid" style="left:70px;height:40px" role="img" aria-label="ネクタイのイラスト"></div>
  <div class="tie dark" style="left:265px;height:28px" role="img" aria-label="ネクタイのイラスト"></div>
  <div class="tie mid" style="left:60px;top:200px;height:150px" role="img" aria-label="ネクタイのイラスト"></div>
  <div class="tie light" style="left:170px;top:380px;height:100px" role="img" aria-label="ネクタイのイラスト"></div>
  <div class="tie dark" style="left:250px;top:560px;height:150px" role="img" aria-label="ネクタイのイラスト"></div>
  <div class="tie mid" style="left:95px;top:660px;height:140px" role="img" aria-label="ネクタイのイラスト"></div>
  <div class="tie light" style="left:430px;top:620px;height:130px" role="img" aria-label="ネクタイのイラスト"></div>
  <div class="tie dark" style="left:560px;top:700px;height:150px" role="img" aria-label="ネクタイのイラスト"></div>
  <div class="tie mid" style="left:665px;top:640px;height:140px" role="img" aria-label="ネクタイのイラスト"></div>
  <div class="tie light" style="left:330px;top:760px;height:90px" role="img" aria-label="ネクタイのイラスト"></div>

  <div class="author">
    <div class="author-name">森川 陽介</div>
    <div class="author-roman">Yosuke Morikawa</div>
  </div>

  <h1 class="title">
    <div class="title-lead">どうして？</div>
    <div class="title-line">腕時計を</div>
    <div class="title-line">磨くと</div>
    <div class="title-line">来店客が</div>
    <div class="title-line">ふえるのか</div>
  </h1>

  <div class="tagline">未来をひらくのは<br>“話術”より</div>
  <div class="keyword">笑顔力</div>

  <div class="gift gift-1">
    <svg class="ribbon" width="310" height="40" viewBox="0 0 310 40">
      <polygon points="0,0 310,0 295,20 310,40 0,40 15,20" fill="var(--orange)"/>
      <text x="155" y="27" text-anchor="middle" font-size="19" font-weight="700" fill="#fff" font-family="Noto Sans JP, sans-serif">読者限定プレゼント ❶</text>
    </svg>
    <div class="gift-note">得たい成果を得る為の</div>
    <div class="gift-item">5ステップテンプレート</div>
  </div>

  <div class="gift gift-2">
    <svg class="ribbon" width="310" height="40" viewBox="0 0 310 40">
      <polygon points="0,0 310,0 295,20 310,40 0,40 15,20" fill="var(--orange)"/>
      <text x="155" y="27" text-anchor="middle" font-size="19" font-weight="700" fill="#fff" font-family="Noto Sans JP, sans-serif">読者限定プレゼント ❷</text>
    </svg>
    <div class="gift-note">失敗しないマスコミでは出さない</div>
    <div class="gift-item">“もの選び”のポイント伝授</div>
  </div>
</div>
</body>
</html>
```